Falcrest security business card

Looking for a business card for my security company

Target Market(s)

Security

Industry/Entity Type

Security

Contact Information for Business Card

Name - Gil Marston. Title - General manager - direct 314 862.4490 website www. falcrestsecurityservices.example email - gil@ falcrestsecurityservices.example

Requirements
Must have
• Logo attached

```html
<!DOCTYPE html>
<html lang="en">
<head>
<meta charset="utf-8">
<title>Falcrest Security Services – Business Card</title>
<link href="https://fonts.googleapis.com/css2?family=Open+Sans:wght@400;600;700&display=swap" rel="stylesheet">
<style>
  :root {
    --backdrop: #2e2e2e;
    --card-white: #f7f7f7;
    --card-black: #070707;
    --ink: #1a1a1a;
    --gold-dark: #8c6a28;
    --gold-light: #f3e2a4;
    --gold-mid: #c9a24e;
    --text-light: #e6e6e6;
  }
  * { margin: 0; padding: 0; box-sizing: border-box; }
  html, body { width: 1200px; height: 900px; overflow: hidden; }
  body {
    background: var(--backdrop);
    font-family: "Open Sans", sans-serif;
    position: relative;
  }
  .card {
    position: absolute;
    width: 560px;
    height: 320px;
    overflow: hidden;
    box-shadow: 0 10px 30px rgba(0,0,0,0.45);
  }
  .gold-band {
    position: absolute;
    left: 0; right: 0; bottom: 0;
    height: 16px;
    background: linear-gradient(90deg, var(--gold-dark) 0%, var(--gold-mid) 30%, var(--gold-light) 55%, var(--gold-mid) 75%, var(--gold-dark) 100%);
  }
  /* Front */
  .card-front {
    left: 80px; top: 100px;
    background: linear-gradient(160deg, #ffffff 0%, var(--card-white) 60%, #e8e8e8 100%);
  }
  .wordmark {
    display: flex;
    align-items: center;
    gap: 12px;
    font-weight: 700;
    letter-spacing: 2px;
    text-transform: uppercase;
  }
  .wordmark-dot {
    width: 18px; height: 18px;
    border-radius: 50%;
  }
  .card-front .wordmark {
    position: absolute;
    left: 0; right: 0; top: 122px;
    justify-content: center;
    font-size: 44px;
    color: var(--ink);
  }
  .card-front .wordmark-dot { background: var(--ink); }
  /* Back */
  .card-back {
    left: 560px; top: 480px;
    background: linear-gradient(115deg, #0c0c0c 0%, var(--card-black) 55%, #111 100%);
  }
  .card-back .wordmark {
    position: absolute;
    right: 40px; top: 50px;
    font-size: 34px;
    color: var(--gold-mid);
  }
  .card-back .wordmark-dot { background: var(--gold-mid); width: 14px; height: 14px; }
  .cat-figure {
    position: absolute;
    right: 30px; top: 150px;
    width: 210px; height: 90px;
    border-radius: 45px 60px 20px 40px;
    background: linear-gradient(90deg, #6f6447 0%, #b5a57a 60%, #8a7b55 100%);
    opacity: 0.8;
  }
  .person {
    position: absolute;
    left: 34px; top: 150px;
  }
  .person-name {
    font-size: 18px;
    font-weight: 700;
    color: var(--gold-mid);
    text-transform: uppercase;
    letter-spacing: 0.5px;
  }
  .person-title {
    font-size: 14px;
    color: var(--text-light);
  }
  .contact-list {
    position: absolute;
    left: 34px; top: 226px;
    list-style: none;
  }
  .contact-list li {
    display: flex;
    align-items: center;
    gap: 10px;
    font-size: 13px;
    color: var(--text-light);
    line-height: 22px;
  }
  .contact-list svg { width: 13px; height: 13px; fill: var(--gold-mid); flex: none; }
</style>
</head>
<body>

  <section class="card card-front">
    <div class="wordmark"><span class="wordmark-dot"></span>Falcrest</div>
    <div class="gold-band"></div>
  </section>

  <section class="card card-back">
    <div class="wordmark"><span class="wordmark-dot"></span>Falcrest</div>
    <div class="cat-figure" role="img" aria-label="Gold silhouette of a leaping big cat"></div>

    <div class="person">
      <p class="person-name">Gil Marston</p>
      <p class="person-title">General manager</p>
    </div>

    <ul class="contact-list">
      <li>
        <svg viewBox="0 0 16 16" aria-hidden="true"><path d="M3 1h3l1.5 4-2 1.5a9 9 0 0 0 4 4L11 8.5l4 1.5v3a2 2 0 0 1-2 2A13 13 0 0 1 1 3a2 2 0 0 1 2-2z"/></svg>
        314 862.4490
      </li>
      <li>
        <svg viewBox="0 0 16 16" aria-hidden="true"><path d="M1 3h14v10H1z M2 4l6 5 6-5" fill="none" stroke="#c9a24e" stroke-width="1.5"/></svg>
        gil@ falcrestsecurityservices.example
      </li>
      <li>
        <svg viewBox="0 0 16 16" aria-hidden="true"><circle cx="8" cy="8" r="6.5" fill="none" stroke="#c9a24e" stroke-width="1.3"/><path d="M1.5 8h13M8 1.5c-3 3.5-3 9.5 0 13M8 1.5c3 3.5 3 9.5 0 13" fill="none" stroke="#c9a24e" stroke-width="1.1"/></svg>
        www. falcrestsecurityservices.example
      </li>
    </ul>

    <div class="gold-band"></div>
  </section>

</body>
</html>
```